Velvet Lantern Poster

Harbor Arts Center for Dance Education presents
The Velvet Lantern
Friday December 19, 2014 7:30 PM
Marlowe Theatre at the College of Brindlewood

```html
<!DOCTYPE html>
<html lang="en">
<head>
<meta charset="utf-8">
<title>The Velvet Lantern</title>
<link rel="stylesheet" href="https://fonts.googleapis.com/css2?family=Oswald:wght@300;400;500;600&display=swap">
<style>
  :root {
    --paper: #f7efe6;
    --paper-edge: #ecd9c6;
    --rust: #6e2219;
    --rust-soft: #c98f74;
    --title-fill: #fbf4ec;
    --frame: #fdfaf6;
    --ink: #1d1412;
    --accent: #d4242a;
  }
  * { margin: 0; padding: 0; box-sizing: border-box; }
  html, body { width: 960px; height: 1200px; overflow: hidden; background: #ffffff; }
  .poster {
    position: relative;
    width: 960px;
    height: 1200px;
    background: radial-gradient(ellipse at center, var(--paper) 55%, var(--paper-edge) 100%);
    font-family: "Oswald", "Arial Narrow", sans-serif;
    color: var(--rust);
  }
  .presenter {
    position: absolute;
    top: 70px; left: 0; width: 100%;
    text-align: center;
    font-weight: 500;
    font-size: 17px;
    letter-spacing: 0.3px;
    text-transform: uppercase;
  }
  .title {
    position: absolute;
    top: 106px; left: 0; width: 100%;
    text-align: center;
    font-weight: 300;
    font-size: 84px;
    line-height: 1;
    letter-spacing: 3px;
    text-transform: uppercase;
    white-space: nowrap;
    color: var(--title-fill);
    -webkit-text-stroke: 2px var(--rust-soft);
    text-shadow: 2px 3px 3px rgba(110, 34, 25, 0.25);
  }
  .photo {
    position: absolute;
    left: 110px; top: 216px;
    width: 740px; height: 578px;
    border: 5px solid var(--frame);
    box-shadow: 0 1px 4px rgba(0,0,0,0.25);
    background: linear-gradient(180deg,
      #3f67a8 0%, #7b8fb0 22%, #e1b870 38%, #d9772e 45%,
      #4a6a8c 50%, #2c3c45 58%, #2c2c26 70%, #5f6670 85%, #8c8f98 100%);
  }
  .rule {
    position: absolute;
    left: 144px; width: 672px;
    border-top: 2px dotted var(--rust);
  }
  .rule.top { top: 830px; }
  .rule.bottom { top: 914px; }
  .date {
    position: absolute;
    top: 832px; left: 144px;
    width: 548px;
    font-weight: 400;
    font-size: 54px;
    letter-spacing: -1px;
    line-height: 80px;
    text-transform: uppercase;
    white-space: nowrap;
  }
  .time-badge {
    position: absolute;
    left: 700px; top: 808px;
    width: 112px; height: 112px;
    border-radius: 50%;
    background: var(--rust);
    color: var(--paper);
    display: flex; flex-direction: column;
    align-items: center; justify-content: center;
    font-weight: 400;
    font-size: 38px;
    line-height: 40px;
    text-transform: uppercase;
  }
  .venue {
    position: absolute;
    top: 938px; left: 0; width: 100%;
    text-align: center;
    font-weight: 500;
    font-size: 28px;
    text-transform: uppercase;
    white-space: nowrap;
  }
  .org {
    position: absolute;
    top: 1012px; left: 0; width: 100%;
    display: flex; align-items: center; justify-content: center;
    gap: 18px;
  }
  .org-dot {
    width: 34px; height: 34px; border-radius: 50%;
    background: var(--accent);
    flex: none;
  }
  .org-name {
    font-weight: 600;
    font-size: 28px;
    line-height: 36px;
    color: var(--ink);
    text-transform: uppercase;
    text-align: center;
  }
</style>
</head>
<body>
  <main class="poster">
    <p class="presenter">Harbor Arts Center for Dance Education presents</p>
    <h1 class="title">The Velvet Lantern</h1>
    <div class="photo" role="img" aria-label="Photograph of a wooden boardwalk leading over dune grass toward the ocean at sunset under a blue and orange sky"></div>
    <div class="rule top"></div>
    <p class="date">Friday December 19, 2014</p>
    <div class="time-badge"><span>7:30</span><span>PM</span></div>
    <div class="rule bottom"></div>
    <p class="venue">Marlowe Theatre at the College of Brindlewood</p>
    <div class="org">
      <span class="org-dot"></span>
      <p class="org-name">Harbor Arts Center<br>for Dance Education</p>
    </div>
  </main>
</body>
</html>
```